5x8" package design for beauty / skin care product in a mylar bag

Brisomel Labs’ Glycolic Acid Powder is pure glycolic acid powder that, when mixed with water, creates glycolic acid solution. Depending on the amount of water added to the powder, you can create different strengths of the solution. Commerical products use between 10 and 70% glycolic acid solution in products. Brisomel Labs is part of the Brisomel hair care company. One of our products use glycolic acid and we can repurpose the raw ingredient alone for retail sales targeting do-it-yourself at home beauty and skin care makers.

Most sellers of glycolic acid powder use basic packaging. Brisomel Labs intends to create professional, standout packaging that reinforces the quality of the glycolic acid powder we are selling and is consistent with other Brisomel brand products sold.

Package design is for a 5x8" matte finished, top loading, resealable pouch. Just looking for front design initially. Second project will include back pouch design using format or design from the front of package.

```html
<!DOCTYPE html>
<html lang="en">
<head>
<meta charset="UTF-8">
<title>Brisomel Labs – Glycolic Acid Powder, Pouch Front</title>
<link href="https://fonts.googleapis.com/css2?family=League+Spartan:wght@400;600;800&family=Allura&display=swap" rel="stylesheet">
<style>
  :root {
    --backdrop: #92aed6;
    --olive: #a89f52;
    --olive-deep: #948b45;
    --teal: #468691;
    --berry: #b0578a;
    --white: #ffffff;
    --powder-light: #f6f5f7;
    --powder-shade: #cfcbd3;
    --wood: #d49a5c;
  }
  * { margin: 0; padding: 0; box-sizing: border-box; }
  html, body {
    width: 1200px;
    height: 834px;
    overflow: hidden;
    background: var(--backdrop);
  }
  .pouch-front {
    position: absolute;
    left: 324px;
    top: 37px;
    width: 551px;
    height: 760px;
    background: var(--olive);
    overflow: hidden;
    font-family: "League Spartan", sans-serif;
    color: var(--white);
  }
  .brand-name {
    position: absolute;
    top: 88px;
    left: 0;
    width: 100%;
    text-align: center;
    font-family: "League Spartan", sans-serif;
    font-weight: 400;
    font-size: 40px;
    letter-spacing: 3px;
    color: var(--white);
  }
  .product-title {
    position: absolute;
    top: 184px;
    left: 0;
    width: 100%;
    text-align: center;
  }
  .product-title .title-main {
    display: block;
    font-weight: 800;
    font-size: 74px;
    line-height: 1;
    letter-spacing: -3px;
    color: var(--teal);
  }
  .product-title .title-script {
    display: block;
    margin-top: -22px;
    font-family: "Allura", cursive;
    font-size: 92px;
    line-height: 1;
    color: var(--white);
  }
  .uses-band {
    position: absolute;
    top: 354px;
    left: 0;
    width: 100%;
    height: 54px;
    background: var(--teal);
    display: flex;
    align-items: center;
    justify-content: center;
    gap: 9px;
    list-style: none;
    font-weight: 600;
    font-size: 12.5px;
    letter-spacing: 0.1px;
  }
  .uses-band li::before {
    content: "•";
    margin-right: 4px;
  }
  .product-photo {
    position: absolute;
    left: 85px;
    top: 415px;
    width: 398px;
    height: 398px;
    border-radius: 50%;
    background:
      radial-gradient(circle at 50% 50%, var(--powder-light) 0%, #ebe9ee 55%, var(--powder-shade) 80%, var(--wood) 82%, #c0824a 100%);
  }
  .badge-free {
    position: absolute;
    left: 382px;
    top: 485px;
    width: 133px;
    height: 44px;
    background: var(--berry);
    border-radius: 14px 4px 14px 4px;
    display: flex;
    align-items: center;
    padding-left: 10px;
    gap: 6px;
  }
  .badge-free .percent {
    font-weight: 800;
    font-size: 24px;
    line-height: 1;
  }
  .badge-free .claim {
    font-weight: 600;
    font-size: 9.5px;
    line-height: 1.1;
  }
  .net-weight {
    position: absolute;
    left: 33px;
    top: 681px;
    width: 127px;
    height: 45px;
    background: var(--berry);
    border-radius: 14px 4px 14px 4px;
    display: flex;
    align-items: center;
    justify-content: center;
    font-weight: 600;
    font-size: 14px;
  }
</style>
</head>
<body>
  <main class="pouch-front">
    <p class="brand-name">Brisomel Labs</p>

    <h1 class="product-title">
      <span class="title-main">GLYCOLIC</span>
      <span class="title-script">Acid Powder</span>
    </h1>

    <ul class="uses-band">
      <li>FACIAL</li>
      <li>TONER</li>
      <li>SCALP SCRUB</li>
      <li>HYPERPIGMENTATION</li>
      <li>RESEALABLE BAG</li>
    </ul>

    <div class="product-photo" role="img" aria-label="Wooden bowl filled with white glycolic acid powder, seen from above"></div>

    <div class="badge-free">
      <span class="percent">0%</span>
      <span class="claim">FRAGRANCES,<br>ADDITIVES, DYES</span>
    </div>

    <div class="net-weight">NET WT. 100G</div>
  </main>
</body>
</html>
```